Sci Fi/ Secret Agent Author needs website design!

My name is Talia Brook and I am an author. I require a site that can provide information about myself and my books and other works.

I would like it to have a Home, blog function, (about the) books/series section so people can visit another section and read about each individual book that's going to be released. A resources page, a Store, social media links and ability to load/embed videos from clipvana and other.

I write mild scifi/thriller/conspiracy/secret government type novels. -At the moment-. The series follows a strong female lead that is an agent with a secret organisation in a classified military installation.

The theme would be professional yet possibly show this element.

Target Market(s)

/military fiction/thriller/fantasy/Sci fi/ femme-fatal, readers. Mostly females, age 18-60
Novel readers

Number of Pages Required

5+ page

Requirements
Must have
• Would like designers to follow brief. :)
• My budget includes all the pages I will need;
• eg home, blog, resources, store, ability to pay with coinlark and Credit Cards
• , ability to have trailers from clipvana etc. Must have links to the social media mentioned in the brief.
Nice to have
• use of the colours I have suggested. electric/indigo purple, fuschia highlights , dark greys
• as I will possibly base branding for social media ETC on the look of your website design and colour scheme.
• Ability for trailer on front page??
Should not have
• Should not be too cluttered. (But I am open to all ideas)

```html
<!DOCTYPE html>
<html lang="en">
<head>
<meta charset="utf-8">
<title>Talia Brook — Author</title>
<link rel="stylesheet" href="https://fonts.googleapis.com/css2?family=Lato:wght@300;400;700&family=Tinos:wght@400;700&display=swap">
<style>
:root{
  --purple:#7b3fa0;
  --purple-dark:#3b2447;
  --purple-input:#4f3262;
  --ink:#222;
  --text:#555;
  --muted:#8a8a8a;
  --light-bg:#efedec;
  --footer-bg:#141016;
  --accent:#e2552b;
  --white:#fff;
}
*{box-sizing:border-box;margin:0;padding:0}
html,body{width:1200px;height:3939px;overflow:hidden}
body{font-family:"Lato",Arial,sans-serif;color:var(--text);background:var(--white);position:relative}
.serif{font-family:"Tinos","Times New Roman",serif}
section,header,footer,.topbar{position:absolute;left:0;width:1200px}
.abs{position:absolute}

/* top bar */
.topbar{top:0;height:32px;background:var(--purple);color:var(--white);font-size:11px}
.topbar .login{left:26px;top:9px;display:flex;align-items:center;gap:6px}
.topbar .search{left:152px;top:8px}
.social{display:flex;gap:12px;font-size:10px;white-space:nowrap}
.topbar .social{right:104px;top:10px}
.topbar .site-mark{right:30px;top:9px;font-size:11px;font-weight:700}

/* header */
.site-header{top:32px;height:249px;background:var(--white)}
.logo{font-family:"Tinos",serif;color:var(--purple);font-size:52px;text-align:center;width:100%;top:48px}
.tagline{width:100%;text-align:center;top:134px;font-size:10px;color:#444}
.nav{top:202px;width:100%;display:flex;justify-content:center;gap:62px;font-size:12px;color:#555;letter-spacing:.5px}

/* hero */
.hero{top:281px;height:467px;background:linear-gradient(120deg,#6d5a4c 0%,#8b7a6c 40%,#5c4b3f 100%)}
.hero-title{left:84px;top:110px;font-size:64px;line-height:80px;color:var(--white)}
.btn-outline{left:84px;top:291px;width:189px;height:48px;border:2px solid var(--white);color:var(--white);font-size:18px;display:flex;align-items:center;justify-content:center}
.hero-book{left:782px;top:26px;width:229px;height:415px;background:linear-gradient(160deg,#b34bb8,#6d2a8c);box-shadow:4px 6px 14px rgba(0,0,0,.35)}

/* about */
.about{top:748px;height:612px;background:var(--light-bg)}
.about-label{right:780px;top:84px;font-size:15px;font-weight:700;color:#444;letter-spacing:1px}
.about-name{right:780px;top:160px;font-size:46px;font-weight:300;color:var(--purple)}
.about-genres{right:780px;top:214px;font-size:9px;color:#444}
.about-text{left:150px;top:270px;width:270px;font-size:13px;line-height:23px;color:#555;text-align:right}
.about .social{right:800px;top:492px;color:#333;font-size:9px;gap:9px}
.author-photo{left:454px;top:87px;width:308px;height:441px;background:linear-gradient(180deg,#f4f4f2,#d9d8d5)}
.thumb{width:96px;height:150px}
.thumb-cap{font-size:13px;color:#222;width:140px;text-align:center}

/* more books */
.books{top:1360px;height:749px;background:var(--white)}
.section-title{width:100%;text-align:center;font-size:32px;color:#222}
.rule{width:50px;height:2px;background:#888;left:575px}
.arrow-btn{width:42px;height:42px}
.book{width:300px;text-align:center}
.book-cover{margin:0 auto;width:184px;height:320px;box-shadow:6px 6px 12px rgba(0,0,0,.25)}
.book-title{margin-top:42px;font-size:14px;font-weight:700;color:#222}
.book-desc{margin:12px auto 0;width:270px;font-size:11px;line-height:16px;color:var(--muted)}
.price{margin-top:16px;font-size:14px;color:var(--accent);font-weight:700}
.buy{margin:18px auto 0;width:152px;height:37px;border:2px solid #333;border-radius:3px;font-size:15px;font-weight:700;color:#222;display:flex;align-items:center;justify-content:center}
.buy.primary{border-color:var(--purple);color:var(--purple)}

/* video + other works */
.media{top:2109px;height:696px;background:var(--light-bg)}
.video{left:63px;top:73px;width:609px;height:549px;background:linear-gradient(135deg,#3b3a6b 0%,#c04a8e 35%,#d88a3c 60%,#3c6f8f 100%);overflow:hidden}
.video-controls{left:0;bottom:0;width:100%;height:52px;background:rgba(20,20,20,.85);color:var(--white);font-size:14px;display:flex;align-items:center;gap:22px;padding:0 22px}
.works-title{left:735px;top:70px;font-size:28px;color:#222}
.work-card{left:735px;width:399px;height:152px;color:var(--white);font-size:20px;line-height:26px;padding:36px 0 0 34px}

/* blog */
.blog{top:2805px;height:745px;background:var(--white)}
.blog-main-img{left:63px;top:162px;width:538px;height:321px;background:linear-gradient(120deg,#6d5443,#9a8472 60%,#c9c2ba)}
.post-title{font-size:15px;font-weight:700;color:#222}
.meta{font-size:12px;color:#444}
.meta .sep{margin:0 10px;color:var(--accent)}
.meta .comments{color:var(--accent)}
.excerpt{font-size:11.5px;line-height:17px;color:var(--muted)}
.read-more{font-size:13px;font-weight:700;color:#222}
.side-post{left:630px;width:520px;height:150px}
.side-thumb{left:0;top:0;width:150px;height:150px}
.side-body{left:168px;top:14px;width:320px}

/* newsletter */
.newsletter{top:3550px;height:121px;background:var(--purple-dark)}
.newsletter h2{left:63px;top:36px;font-size:38px;font-weight:400;color:var(--white);letter-spacing:1px}
.nl-input{left:670px;top:37px;width:281px;height:47px;background:var(--purple-input)}
.nl-btn{left:951px;top:37px;width:152px;height:47px;background:var(--purple);color:var(--white);font-size:16px;font-weight:700;display:flex;align-items:center;justify-content:center}

/* footer */
.site-footer{top:3671px;height:268px;background:var(--footer-bg);color:#777}
.site-footer .logo{top:40px;font-size:46px}
.site-footer .tagline{top:96px;color:#999}
.site-footer .social{top:130px;left:0;width:100%;justify-content:center;color:#888}
.site-footer .nav{top:176px;color:#777;gap:62px}
.copyright{top:220px;width:100%;text-align:center;font-size:11px;color:#555}
</style>
</head>
<body>

<div class="topbar">
  <div class="abs login">
    <svg width="13" height="13" viewBox="0 0 13 13"><circle cx="6.5" cy="4" r="3" fill="#fff"/><path d="M1 13c0-3.5 2.5-5 5.5-5s5.5 1.5 5.5 5z" fill="#fff"/></svg>
    <span>Login</span>
  </div>
  <svg class="abs search" width="15" height="15" viewBox="0 0 15 15"><circle cx="6" cy="6" r="4.5" stroke="#fff" stroke-width="1.8" fill="none"/><line x1="9.5" y1="9.5" x2="14" y2="14" stroke="#fff" stroke-width="1.8"/></svg>
  <div class="abs social"><span>Bondly</span><span>Chirpwave</span><span>Snapsy</span><span>Pinora</span><span>clipvana</span><span>Circlet</span></div>
  <div class="abs site-mark">Plenvo</div>
</div>

<header class="site-header">
  <div class="abs logo">Talia Brook</div>
  <div class="abs tagline">I am an Author</div>
  <nav class="abs nav"><span>HOME</span><span>ABOUT</span><span>BOOKS</span><span>STORE</span><span>BLOG</span><span>CONTACT</span></nav>
</header>

<section class="hero" role="img" aria-label="Photo of a wooden desk with colourful pens and notebooks">
  <div class="abs hero-title serif">Lorem ipsum dolor<br>sit amet consect</div>
  <div class="abs btn-outline">Learn More</div>
  <div class="abs hero-book" role="img" aria-label="Purple cover of a featured book"></div>
</section>

<section class="about">
  <div class="abs about-label serif">ABOUT AUTHOR</div>
  <div class="abs about-name">Talia Brook</div>
  <div class="abs about-genres">Mild scifi, Thriller, Conspiracy, Secret Government</div>
  <p class="abs about-text">Lorem ipsum dolor sit amet, consec tetuer adipiscing elit. Aenean commodo ligula eget dolor. Aenean massa. Cum sociis natoque penatibus et magnis Lorem ipsum dolor sit amet, consec tetuer adipiscing elit.. Cum sociisna toque penatibus et magnis...</p>
  <div class="abs social"><span>Bondly</span><span>Chirpwave</span><span>Snapsy</span><span>Pinora</span><span>clipvana</span><span>Circlet</span></div>
  <div class="abs author-photo" role="img" aria-label="Portrait photo of the author seated in a bright room"></div>

  <div class="abs thumb" style="left:830px;top:87px;background:linear-gradient(160deg,#3f5a45,#6f7a52)" role="img" aria-label="Green book cover"></div>
  <div class="abs thumb-cap" style="left:808px;top:265px">LOREM IPSM</div>
  <div class="abs thumb" style="left:993px;top:87px;background:linear-gradient(160deg,#5b3a66,#c67a45)" role="img" aria-label="Book cover with food photo"></div>
  <div class="abs thumb-cap" style="left:971px;top:265px">OREM IPSM</div>
  <div class="abs thumb" style="left:830px;top:329px;background:linear-gradient(160deg,#f4f4f2,#dfe3dc)" role="img" aria-label="Pale book cover"></div>
  <div class="abs thumb-cap" style="left:808px;top:505px">MOREM IPS</div>
  <div class="abs thumb" style="left:993px;top:329px;background:linear-gradient(160deg,#6a3d9a,#3c2a6b)" role="img" aria-label="Purple book cover"></div>
  <div class="abs thumb-cap" style="left:971px;top:505px">MOREM IPS</div>
</section>

<section class="books">
  <h2 class="abs section-title serif" style="top:56px;font-weight:400">More Books From This Other</h2>
  <div class="abs rule" style="top:106px"></div>
  <svg class="abs arrow-btn" style="left:1037px;top:61px" viewBox="0 0 42 42"><circle cx="21" cy="21" r="19" fill="none" stroke="#7b3fa0" stroke-width="2"/><path d="M24 13l-8 8 8 8" fill="none" stroke="#7b3fa0" stroke-width="2.5"/></svg>
  <svg class="abs arrow-btn" style="left:1092px;top:61px" viewBox="0 0 42 42"><circle cx="21" cy="21" r="19" fill="none" stroke="#7b3fa0" stroke-width="2"/><path d="M18 13l8 8-8 8" fill="none" stroke="#7b3fa0" stroke-width="2.5"/></svg>

  <div class="abs book" style="left:99px;top:158px">
    <div class="book-cover" style="background:linear-gradient(170deg,#2fa3c8,#1d6a8a 60%,#4a5a3a)" role="img" aria-label="Blue book cover"></div>
    <div class="book-title">Harbor Cipher</div>
    <p class="book-desc">Rem ipsum dolor sit amet consectetur adipiscing elit cupidatat non proident suncup animest</p>
    <div class="price">£201.30</div>
    <div class="buy primary">Buy Now</div>
  </div>
  <div class="abs book" style="left:451px;top:158px">
    <div class="book-cover" style="background:linear-gradient(180deg,#1f3a4a,#1a2530 70%,#0e1418)" role="img" aria-label="Dark night-scene book cover"></div>
    <div class="book-title">Signal Lost</div>
    <p class="book-desc">Rem ipsum dolor sit amet consectetur adipiscing elit cupidatat non proident suncup animest</p>
    <div class="price">£300.00</div>
    <div class="buy">Buy Now</div>
  </div>
  <div class="abs book" style="left:816px;top:158px">
    <div class="book-cover" style="background:linear-gradient(180deg,#ee2e4e,#d8203f 70%,#3a1016)" role="img" aria-label="Red book cover"></div>
    <div class="book-title">The Quiet Base</div>
    <p class="book-desc">Rem ipsum dolor sit amet consectetur adipiscing elit cupidatat non proident suncup animest</p>
    <div class="price">£540.50</div>
    <div class="buy">Buy Now</div>
  </div>
</section>

<section class="media">
  <div class="abs video" role="img" aria-label="Video trailer still with vivid painted colours">
    <svg class="abs" style="left:269px;top:238px" width="72" height="72" viewBox="0 0 72 72"><circle cx="36" cy="36" r="34" fill="rgba(20,20,20,.75)"/><path d="M28 22l22 14-22 14z" fill="#fff"/></svg>
    <div class="abs video-controls">
      <svg width="14" height="16" viewBox="0 0 14 16"><rect x="1" y="1" width="4" height="14" fill="#fff"/><rect x="9" y="1" width="4" height="14" fill="#fff"/></svg>
      <svg width="20" height="16" viewBox="0 0 20 16"><path d="M1 5h4l5-4v14l-5-4H1z" fill="#fff"/><path d="M13 4q3 4 0 8" stroke="#fff" stroke-width="1.6" fill="none"/></svg>
      <span>0:00 / 9:51</span>
      <span style="flex:1"></span>
      <svg width="16" height="16" viewBox="0 0 16 16"><circle cx="8" cy="8" r="6" stroke="#fff" stroke-width="2" fill="none"/></svg>
      <svg width="22" height="14" viewBox="0 0 22 14"><rect x="1" y="1" width="20" height="12" rx="2" stroke="#fff" stroke-width="1.6" fill="none"/></svg>
      <svg width="16" height="16" viewBox="0 0 16 16"><circle cx="8" cy="8" r="3" fill="#fff"/><circle cx="8" cy="8" r="6.5" stroke="#fff" stroke-width="2" stroke-dasharray="3 2" fill="none"/></svg>
      <span style="font-weight:700">clipvana</span>
      <svg width="16" height="16" viewBox="0 0 16 16"><path d="M1 5V1h4M11 1h4v4M15 11v4h-4M5 15H1v-4" stroke="#fff" stroke-width="2" fill="none"/></svg>
    </div>
  </div>
  <h3 class="abs works-title serif" style="font-weight:400">Outher Works</h3>
  <div class="abs work-card" style="top:144px;background:linear-gradient(120deg,#6a2f8f,#c65ab0 60%,#8f3f9f)" role="img" aria-label="Purple misty landscape">Lorem ipsum dolor<br>sit amet consec</div>
  <div class="abs work-card" style="top:310px;background:linear-gradient(120deg,#2e6a3e,#4f8d4a 50%,#2f6f86)" role="img" aria-label="Green painted landscape">Lorem ipsum dolor<br>sit amet consec</div>
  <div class="abs work-card" style="top:475px;background:linear-gradient(120deg,#b7b7b7,#d6d3cf 60%,#5a4a3a)" role="img" aria-label="Still life with a bottle">Lorem ipsum dolor<br>sit amet consec</div>
</section>

<section class="blog">
  <h2 class="abs section-title serif" style="top:60px;font-weight:400">Blog</h2>
  <div class="abs rule" style="top:118px"></div>

  <div class="abs blog-main-img" role="img" aria-label="Book on a wooden table with flowers and coffee"></div>
  <div class="abs post-title" style="left:63px;top:504px">How To Write A Successful Books</div>
  <div class="abs meta" style="left:63px;top:538px">20-Aug-2016<span class="sep">|</span><span class="comments">20 Comments</span></div>
  <p class="abs excerpt" style="left:63px;top:570px;width:538px">Rem ipsum dolor sit amet, consectetur adipiscing elit seddoeius modam empor incididunt labore lore magna aliqua minimsatis veniam Excepteur sint occaecat cupidatat non proident sun culpa asenunt mollit animest [...]</p>
  <div class="abs read-more" style="left:63px;top:651px">Read More</div>

  <div class="abs side-post" style="top:162px">
    <div class="abs side-thumb" style="background:linear-gradient(150deg,#f0ece6,#8a5a3e 70%,#3c2a22)" role="img" aria-label="Person walking with a bicycle"></div>
    <div class="abs side-body">
      <div class="post-title" style="font-size:13px">The Book Of Scilence: You Will Find It</div>
      <div class="meta" style="margin-top:14px;font-size:11px">19-Aug-2016<span class="sep">|</span><span class="comments">10 Comments</span></div>
      <p class="excerpt" style="margin-top:14px">Rem ipsum dolor sit amet, consectetur adipisicing elit cupidatat non proident sun culp animest [...]</p>
    </div>
  </div>
  <div class="abs side-post" style="top:341px">
    <div class="abs side-thumb" style="background:linear-gradient(150deg,#d98a3a,#f0e9df 55%,#c77a34)" role="img" aria-label="Open book on an orange surface"></div>
    <div class="abs side-body">
      <div class="post-title" style="font-size:13px">Never Been Much Reader Until This Book</div>
      <div class="meta" style="margin-top:14px;font-size:11px">19-Aug-2016<span class="sep">|</span><span class="comments">05 Comments</span></div>
      <p class="excerpt" style="margin-top:14px">Rem ipsum dolor sit amet, consectetur adipisicing elit cupidatat non proident sun culp animest [...]</p>
    </div>
  </div>
  <div class="abs side-post" style="top:520px">
    <div class="abs side-thumb" style="background:linear-gradient(150deg,#f2e4c8,#c9a98a 50%,#8a6a5a)" role="img" aria-label="Person reading outdoors in warm light"></div>
    <div class="abs side-body">
      <div class="post-title" style="font-size:13px">How Start Writing or Where is My Coffee?</div>
      <div class="meta" style="margin-top:14px;font-size:11px">19-Aug-2016<span class="sep">|</span><span class="comments">0 Comments</span></div>
      <p class="excerpt" style="margin-top:14px">Rem ipsum dolor sit amet, consectetur adipisicing elit cupidatat non proident sun culp animest [...]</p>
    </div>
  </div>
</section>

<section class="newsletter">
  <h2 class="abs serif">JOIN NEWSLETTER!</h2>
  <div class="abs nl-input"></div>
  <div class="abs nl-btn">SUBSCRIBE</div>
</section>

<footer class="site-footer">
  <div class="abs logo">Talia Brook</div>
  <div class="abs tagline">I am an Author</div>
  <div class="abs social"><span>Bondly</span><span>Chirpwave</span><span>Snapsy</span><span>Pinora</span><span>clipvana</span><span>Circlet</span></div>
  <nav class="abs nav"><span>HOME</span><span>ABOUT</span><span>BOOKS</span><span>STORE</span><span>BLOG</span><span>CONTACT</span></nav>
  <div class="abs copyright">Copyright © 2017 All Rights Reserved.</div>
</footer>

</body>
</html>
```